Flyer design for Trail Beside Outback Trips

We need a new flyer for our tour business. Sketch hive produced a great flyer for us 4 years ago but it is time to update. We have had a price increase that needs to be reflected but we have noticed an issue with our current marketing.
Our tour is a "tagalong" tour which means you follow in your own vehicle. Unfortunately most people associate "tagalong" with 4wd (Four wheel drive vehicles). This is not the case for our tour which can be done in ANY type of vehicle. We need to get across at first glance that this tour is available to all vehicle types. We also need to stress that there is NOT MUCH DRIVING. We cover around 20km total of very easy driving. We go from point of interest to point of interest.
We want our customers to feel that this tour will be a better option than selecting a bus type tour because they use their own vehicle. Our option is also MUCH cheaper than bus options but provides a premium product. It's "cheap" but not cheap if you understand.
I will upload our previous flyer so you have an idea of what we do and how we have been presenting it. We are currently single sided DL but do not mind if we go into double sided DL if you feel that will enable you to share more information. Our price is $50 and half price for kids (as per old flyer)
Some things to remember when trying to appeal to our customer:
Choose a design that clearly communicates that our tagalong tour is suitable for all types of vehicles. For example, "Vehicle-Friendly Tagalong Tour" or "All-Vehicle Tagalong Tour".
Use clear language: Avoid using terms like "off-road" or "4x4" that may imply that our tour is only suitable for certain types of vehicles. Instead, use language that is inclusive and clearly communicates that all vehicles are welcome.
Include photos and videos of a variety of vehicles: This will show potential customers that our tagalong tour is not limited to four-wheel drive vehicles and that any type of vehicle can participate.
Highlight the benefits of a tagalong tour over a bus tour: Emphasise the flexibility and freedom that a tagalong tour offers, as well as the opportunity to explore off-the-beaten-path destinations that are not accessible by bus.
By incorporating these elements into your product presentation, you can avoid confusion and clearly communicate that our tagalong tour is suitable for any type of vehicle, while also highlighting the unique benefits of this type of tour.
Along with the emphasis on all vehicles you need to be clear about what we offer on the tour.
- The excitement of an opal mine tour with an award winning guide and opal miner.
- The wonder of an underground home and discovering how people live in an underground environment.
- Driving through the opal mining area for a close up view of the field.
- Our EXCLUSIVE opal cutting and polishing demonstration.
- The adventure of looking for your own opal.
For further information visit our web site "http://trailbeside.outbackway.example". Check our facebook page "https://www.kinpage.example/trailbesideoutbacktrips". Search Seekora for "Coober Pedy", Trail beside Outback Coober Pedy" or "Coober Pedy Opal mining" to source images of our town and opals.
PLEASE ALSO FIND SOMEWHERE TO SAY "FREE UNPOWERED CAMPING AT TALMO'S WITH ALL TOURS AS WELL AS DISCOUNTS ON POWERED CAMPING" and make this stand out somehow. (http://stay-belowgrid.example.au)

Target Market(s)

18 to 80

Industry/Entity Type

Tourism

Font styles to use
Serif

Colors

Designer to choose colors to be used in the design.

Requirements
Must have
• Eye catching images and attention grabbing headlines
Nice to have
• Modern design.
Should not have
• References to 4wd or buses.

```html
<!DOCTYPE html>
<html lang="en">
<head>
<meta charset="utf-8">
<title>Trail Beside Outback Trips – Vehicle-Friendly Tagalong Flyer</title>
<link rel="stylesheet" href="https://fonts.googleapis.com/css2?family=Montserrat:wght@400;500;600;700;800;900&display=swap">
<style>
  :root {
    --blue: #0b57b0;
    --blue-deep: #08408a;
    --orange: #f5820b;
    --grey: #a9abad;
    --peach: #f3c79a;
    --ink: #1c1c1c;
    --paper: #ffffff;
    --stage: #f1f1f1;
  }
  * { margin: 0; padding: 0; box-sizing: border-box; }
  html, body { width: 1200px; height: 1200px; overflow: hidden; }
  body {
    background: var(--stage);
    font-family: "Montserrat", Arial, sans-serif;
    color: var(--ink);
    position: relative;
  }
  .flyer {
    position: absolute;
    left: 357px; top: 83px;
    width: 486px; height: 1035px;
    background: var(--paper);
    overflow: hidden;
  }
  .abs { position: absolute; }

  .hero-photo {
    left: 0; top: 0; width: 486px; height: 290px;
    background: linear-gradient(180deg, #4d93d6 0%, #8cbbe6 40%, #b9a58c 72%, #9a7b5c 100%);
  }
  .shapes { left: 0; top: 0; width: 486px; height: 1035px; }

  .brand-badge {
    left: 20px; top: 18px; width: 76px; height: 76px; border-radius: 50%;
    background: var(--orange); color: #fff;
    display: flex; align-items: center; justify-content: center; text-align: center;
    font-size: 11px; font-weight: 800; line-height: 1.1;
  }
  .contact-box {
    left: 283px; top: 10px; width: 203px; height: 72px;
    background: var(--paper); border-radius: 8px 0 0 8px;
    padding: 9px 0 0 8px;
    font-size: 11px; font-weight: 700; line-height: 15px; color: var(--ink);
  }
  .contact-box .follow { margin-top: 11px; display: flex; align-items: center; gap: 6px; }
  .contact-box .follow span { margin-right: 7px; }
  .social-square { width: 17px; height: 17px; border-radius: 4px; background: var(--ink); }

  .photo-circle { border-radius: 50%; border: 3px solid var(--orange); }
  .circle-left { left: 80px; top: 284px; width: 96px; height: 96px; background: radial-gradient(circle, #c9a47c, #6e5a46); }
  .circle-main { left: 162px; top: 252px; width: 164px; height: 164px; background: radial-gradient(circle, #5b4a42, #1b1614); }
  .circle-right { left: 319px; top: 286px; width: 92px; height: 92px; background: radial-gradient(circle, #6d8fd6, #0d1a4a); }

  .headline {
    left: 0; width: 486px; top: 424px; text-align: center;
    font-size: 24px; font-weight: 800; color: var(--blue); letter-spacing: -0.3px;
  }
  .subhead {
    left: 130px; width: 240px; top: 453px;
    display: flex; align-items: center; gap: 8px;
    font-size: 15px; font-weight: 700; color: var(--orange); letter-spacing: 2px;
  }
  .subhead::before, .subhead::after { content: ""; flex: 1; height: 3px; background: var(--grey); }
  .intro {
    left: 84px; width: 318px; top: 480px; text-align: center;
    font-size: 8.5px; line-height: 11px; color: #333;
  }

  .price-label {
    left: 83px; top: 511px; padding: 2px 6px;
    background: var(--blue); color: #fff;
    font-size: 11.5px; font-weight: 800;
    box-shadow: 0 4px 0 var(--orange);
  }
  .price {
    left: 185px; top: 498px;
    font-size: 64px; font-weight: 900; color: var(--blue); letter-spacing: -1px;
    text-shadow: 3px 3px 0 var(--orange);
  }
  .price-note {
    left: 302px; top: 566px; width: 98px; padding: 1px 2px;
    background: var(--blue); color: #fff; text-align: center;
    font-size: 5px; font-weight: 800; line-height: 6px;
  }

  .banner {
    background: var(--blue); color: #fff; text-align: center;
    transform: skewX(-10deg);
    box-shadow: 0 6px 0 var(--orange);
  }
  .banner > span { display: block; transform: skewX(10deg); }
  .banner-benefits { left: 89px; top: 587px; width: 302px; height: 36px; padding-top: 2px; font-size: 13.5px; font-weight: 800; letter-spacing: 1.2px; line-height: 16px; }
  .banner-features { left: 89px; top: 692px; width: 300px; height: 38px; padding-top: 4px; font-size: 23px; font-weight: 800; letter-spacing: 2px; line-height: 30px; }

  .benefit-pill {
    top: 649px; width: 111px; height: 21px;
    background: linear-gradient(180deg, #1765c0, var(--blue-deep));
    border-radius: 2px; color: #fff; text-align: center;
    font-size: 11.5px; font-weight: 800; letter-spacing: 1px; line-height: 21px;
  }
  .pill-1 { left: 37px; } .pill-2 { left: 182px; } .pill-3 { left: 326px; }

  .feature-list {
    left: 20px; top: 750px; width: 450px; list-style: none;
    font-size: 7.6px; font-weight: 600; letter-spacing: 0.7px; line-height: 10px; text-transform: uppercase;
  }
  .feature-list li { margin-bottom: 7.5px; }

  .camping {
    left: 0; width: 486px; top: 857px; text-align: center;
    font-size: 12px; font-weight: 800; letter-spacing: 0.9px; color: var(--blue); line-height: 17px;
  }
  .camping .venue { color: var(--orange); font-size: 18px; }

  .info-tag {
    top: 946px; width: 163px; height: 20px;
    background: var(--blue); color: #fff; text-align: center;
    transform: skewX(-10deg); box-shadow: 0 3px 0 var(--orange);
    font-size: 6.5px; font-weight: 800; line-height: 8px; padding-top: 2px;
  }
  .info-tag span { display: block; transform: skewX(10deg); }
  .tag-left { left: 25px; } .tag-right { left: 302px; }
  .link {
    top: 978px; font-size: 9.5px; font-weight: 700; letter-spacing: 0.5px; line-height: 11px; color: var(--ink);
  }
  .link-left { left: 20px; } .link-right { left: 298px; }
</style>
</head>
<body>
  <main class="flyer">
    <div class="abs hero-photo" role="img" aria-label="Photo of tour guests beside a mix of everyday cars and utes parked in an outback town"></div>

    <svg class="abs shapes" viewBox="0 0 486 1035" aria-hidden="true">
      <path d="M0,290 L486,290 L486,430 Q243,300 0,430 Z" fill="var(--paper)"/>
      <path d="M0,255 Q75,268 112,330 Q55,370 0,455 Z" fill="var(--blue)"/>
      <path d="M0,455 Q55,370 112,330 L118,342 Q62,385 0,478 Z" fill="var(--orange)"/>
      <path d="M0,478 Q62,385 118,342 L124,356 Q70,405 0,500 Z" fill="var(--grey)"/>
      <path d="M486,255 Q411,268 374,330 Q431,352 486,420 Z" fill="var(--blue)"/>
      <path d="M486,420 Q431,352 374,330 L368,342 Q426,370 486,445 Z" fill="var(--orange)"/>
      <path d="M486,445 Q426,370 368,342 L362,356 Q420,390 486,468 Z" fill="var(--grey)"/>
      <path d="M0,1035 L0,1000 Q170,880 486,940 L486,1035 Z" fill="var(--peach)"/>
      <path d="M30,1035 Q190,920 486,965 L486,1035 Z" fill="var(--grey)"/>
      <path d="M0,1000 Q60,950 120,935 Q60,960 0,1020 Z" fill="#e9e9ea"/>
    </svg>

    <div class="abs brand-badge">Trail<br>Beside</div>

    <div class="abs contact-box">
      <div>PHONE: 08 5550 1234</div>
      <div>trailbeside.outbackway.example</div>
      <div class="follow"><span>FOLLOW US</span><i class="social-square"></i><i class="social-square"></i></div>
    </div>

    <div class="abs photo-circle circle-left" role="img" aria-label="Photo of visitors exploring an opal mine tunnel"></div>
    <div class="abs photo-circle circle-right" role="img" aria-label="Photo of opals glowing under ultraviolet light"></div>
    <div class="abs photo-circle circle-main" role="img" aria-label="Photo of a tour group holding opal finds underground"></div>

    <h1 class="abs headline">VEHICLE-FRIENDLY</h1>
    <div class="abs subhead">TAGALONG</div>
    <p class="abs intro">Our tagalong tour is not limited to four-wheel drive vehicles and that any type of vehicle can participate.</p>

    <div class="abs price-label">OUR PRICE IS</div>
    <div class="abs price">$50</div>
    <div class="abs price-note">AND HALF PRICE FOR<br>KIDS FREE FOR UNDER 5</div>

    <div class="abs banner banner-benefits"><span>THE BENEFITS OF A TAGALONG<br>TOUR OVER A BUS TOUR</span></div>
    <div class="abs benefit-pill pill-1">EMPHASISE</div>
    <div class="abs benefit-pill pill-2">FLEXIBILITY</div>
    <div class="abs benefit-pill pill-3">FREEDOM</div>

    <h2 class="abs banner banner-features"><span>FEATURES OF TOUR</span></h2>

    <ul class="abs feature-list">
      <li>The excitement of an opal mine tour with an award winning guide and opal miner.</li>
      <li>The wonder of an underground home and discovering how people live in an underground environment</li>
      <li>Driving through the opal mining area for a close up view of the field.</li>
      <li>Our exclusive opal cutting and polishing demonstration.</li>
      <li>The adventure of looking for your own opal.</li>
    </ul>

    <p class="abs camping">FREE UNPOWERED CAMPING AT <span class="venue">TALMO'S</span> WITH ALL TOURS<br>AS WELL AS DISCOUNTS ON POWERED CAMPING</p>

    <div class="abs info-tag tag-left"><span>FOR FURTHER INFORMATION<br>VISIT OUR WEB SITE</span></div>
    <div class="abs info-tag tag-right"><span>FOR FURTHER INFORMATION<br>VISIT OUR WEB SITE</span></div>
    <div class="abs link link-left">http://trailbeside.outbackway.example</div>
    <div class="abs link link-right">https://www.kinpage.example/<br>trailbesideoutbacktrips</div>
  </main>
</body>
</html>
```